Dentist's Office needs desktop and mobile website design

This is a turnkey project where we are looking for a bright, elegant, modern website design, both for desktop and mobile. Our existing website is hosted on Pelvora pages. We also require the new design to be set up and fully functional - both desktop and mobile - on Pelvora pages. If Pelvora pages is too limiting, its ok to use a platform like Brelt or Ondalayer. If using these, we will need you to point our domain to the new Brelt site, and hand us the credentials so we can continue to update the site.

We want to continue using our current logo so the new website colors need to go with the logo. Our existing website can be found at www.brightmolar.com.

We want the new website to have the following pages:
1. Home - similar content to our current home page at http://www.brightmolar.com

We also have pictures of our office and team that we would like to show up on the home page in a collage, slide show, or some other creative. Pictures can be found here: https://files.pelvora.net/share?id=7KQ2MWRZ4HVN8TLXBDPAJC3YEFGS&mode=view

Not all pictures have to be used; use as many as needed.

In addition to the content on our current home page, we would like a small section for dental quotes where we could rotate quotes. Sample quotes can be found at http://www.sayingnook.net/dental.html

If above content is too much to fit on one page, it is ok to split into two.

2. Our team - similar to http://www.brightmolar.com/our-dentist-1 . In addition, we want short bios and pictures of other staff added to this page. Pictures and bios can be found here: https://files.pelvora.net/share?id=7KQ2MWRZ4HVN8TLXBDPAJC3YEFGS&mode=view

3. Reviews - similar to http://www.brightmolar.com/patient-testimonials-1

4. Services - provide a summary of services we provide from http://www.brightmolar.com/dental-services . No need for detailed pages pages for each treatment we have on our current website.

5. Contact Us - http://www.brightmolar.com/contact-us

Target Market(s)

local population

Industry/Entity Type

Healthcare

Coding

Coded - Design and coding required

Number of Pages Required

5+ page

Font styles to use
Sans Serif

Requirements
Nice to have
• animated icons would be cool

```html
<!DOCTYPE html>
<html lang="en">
<head>
<meta charset="utf-8">
<title>Sunvale Dental Care</title>
<link href="https://fonts.googleapis.com/css2?family=Lato:ital,wght@0,400;0,700;1,400&family=Questrial&display=swap" rel="stylesheet">
<style>
:root{
  --orange:#ec8a2c;
  --orange-dark:#d9741a;
  --ink:#555;
  --ink-soft:#777;
  --line:#e3e3e3;
  --band:#f3f3f3;
  --bar:#444;
  --white:#fff;
}
*{box-sizing:border-box;margin:0;padding:0}
html,body{width:758px;height:1200px;overflow:hidden;background:var(--white)}
body{position:relative;font-family:'Lato',sans-serif;color:var(--ink)}
.abs{position:absolute}
.display{font-family:'Questrial',sans-serif}
.accent{color:var(--orange)}

/* header */
.brand{left:102px;top:12px;display:flex;align-items:center;gap:8px}
.brand-dot{width:16px;height:16px;border-radius:50%;background:var(--orange)}
.brand-name{font-family:'Questrial',sans-serif;color:var(--orange);font-size:22px;line-height:24px;letter-spacing:1px}
.call{right:103px;top:12px;font-size:9px;color:var(--ink-soft);display:flex;align-items:center;gap:4px}
.call strong{font-size:12.5px;color:var(--ink);letter-spacing:.5px}
.nav{right:103px;top:41px;display:flex;gap:18px;font-family:'Questrial',sans-serif;font-size:11px;color:var(--ink);border-bottom:2px solid var(--orange);padding:0 2px 7px}
.nav a{color:inherit;text-decoration:none}
.nav .current{color:var(--orange)}

/* hero */
.hero{left:0;top:80px;width:758px;height:272px;background:linear-gradient(90deg,#6d5a4d 0%,#b8a79a 30%,#4a4343 55%,#9b8c86 80%,#d6d2cf 100%)}
.hero-caption{left:0;top:256px;width:758px;text-align:center;color:var(--white);font-weight:700;font-size:21px;text-shadow:0 1px 4px rgba(0,0,0,.6)}
.arrow{top:208px}
.booking{left:0;top:299px;width:758px;height:53px;background:rgba(50,50,50,.85)}
.booking h2{position:absolute;top:6px;width:100%;text-align:center;color:var(--white);font-size:11px;letter-spacing:.5px;font-weight:700}
.field{position:absolute;top:28px;height:18px;background:var(--white);font-size:7.5px;color:var(--ink-soft);padding:5px 6px;border-radius:2px}
.submit{position:absolute;top:27px;left:584px;width:71px;height:20px;background:var(--orange);border:1px solid var(--white);color:var(--white);font-size:9px;font-weight:700;text-align:center;line-height:18px;border-radius:2px}

/* welcome */
.welcome-title{left:103px;top:380px;font-size:18px;color:var(--ink)}
.welcome-title::after{content:"";display:block;width:384px;height:1px;background:var(--line);margin-top:4px}
.welcome-text{left:103px;top:410px;width:384px;font-size:8.2px;line-height:16px;color:var(--ink-soft)}
.read-more{left:449px;top:496px;font-size:7.5px;font-style:italic;color:var(--orange);text-decoration:underline}
.team-photo{left:503px;top:373px;width:148px;height:148px;border-radius:50%;border:2px solid var(--orange);background:radial-gradient(circle at 50% 30%,#f6a54a,#e58a34 55%,#9c6b52)}

/* services */
.band{left:0;top:531px;width:758px;height:258px;background:var(--band)}
.section-title{font-family:'Questrial',sans-serif;font-size:18px;color:var(--ink)}
.section-rule{height:1px;background:var(--line)}
.service{display:flex;align-items:center;gap:8px;font-family:'Questrial',sans-serif;font-size:12px;color:var(--ink)}
.service svg{flex:none}
.service.active{color:var(--orange)}
.hours{left:485px;top:590px;width:170px;font-size:8.5px;color:var(--ink-soft)}
.hours tr td{padding:2.4px 0}
.hours td:nth-child(2){width:10px}
.hours td:nth-child(3){color:var(--ink);font-weight:700}
.emergency{left:485px;top:709px;width:170px;font-size:7px;line-height:10.5px;color:var(--ink-soft)}
.hours-phone{left:485px;top:740px;display:flex;gap:6px;align-items:center;font-size:11.5px;color:var(--orange);font-weight:700}

/* testimonial */
.quote-box{left:103px;top:867px;width:465px;height:60px;background:var(--white);border:1px solid var(--line);border-radius:2px;box-shadow:0 1px 4px rgba(0,0,0,.06);padding:9px 12px;font-size:7.6px;line-height:14.5px;font-style:italic;color:var(--ink)}
.quote-mark{font-size:20px;color:#bbb;font-style:normal;line-height:0;vertical-align:-6px;margin-right:3px}
.avatar{left:575px;top:864px;width:70px;height:70px;border-radius:50%;border:4px solid var(--white);box-shadow:0 1px 5px rgba(0,0,0,.2);background:radial-gradient(circle at 50% 40%,#d9c1a9,#8a9aa8 70%,#c8d3db)}
.patient{left:492px;top:944px;font-size:10px;font-weight:700;color:#333}

/* members */
.members{left:0;top:984px;width:758px;height:55px;background:var(--band)}
.badge{position:absolute;top:14px;height:26px;border-radius:4px}

/* footer */
.footer{left:0;top:1039px;width:758px;height:138px;background:var(--orange);color:var(--white)}
.f-head{position:absolute;top:29px;font-size:8.5px;font-weight:700}
.f-rule{position:absolute;top:43px;height:1px;background:rgba(255,255,255,.35)}
.f-links{position:absolute;left:105px;top:52px;list-style:none;font-size:7.5px;line-height:16.2px}
.f-contact{position:absolute;left:197px;top:52px;font-size:7.5px;line-height:11.5px}
.f-contact div{display:flex;gap:6px;margin-bottom:6px}
.map{position:absolute;left:348px;top:51px;width:155px;height:73px;border:2px solid #d9d9d9;background:linear-gradient(135deg,#eee8dd,#e4e0d6)}
.v-div{position:absolute;top:27px;width:1px;height:90px;background:rgba(255,255,255,.3)}
.f-brand{position:absolute;left:549px;top:55px;display:flex;align-items:center;gap:7px}
.f-brand .brand-name{color:var(--white);font-size:18px;line-height:19px}
.f-brand .brand-dot{background:var(--white)}
.social{position:absolute;top:106px;width:14px;height:14px;background:#c8321e;border-radius:2px}
.copyright{left:0;top:1177px;width:758px;height:23px;background:#666;color:#eee;font-size:8px;text-align:center;line-height:23px}
</style>
</head>
<body>

<header>
  <div class="abs brand">
    <span class="brand-dot"></span>
    <span class="brand-name">sunvale<br>dental care</span>
  </div>
  <div class="abs call">CALL US!
    <svg width="11" height="11" viewBox="0 0 24 24"><path fill="#ec8a2c" d="M6.6 10.8a15 15 0 006.6 6.6l2.2-2.2a1 1 0 011-.25 11.4 11.4 0 003.6.6 1 1 0 011 1V20a1 1 0 01-1 1A17 17 0 013 4a1 1 0 011-1h3.5a1 1 0 011 1c0 1.25.2 2.45.6 3.6a1 1 0 01-.25 1z"/></svg>
    <strong>209-555-0148</strong></div>
  <nav class="abs nav">
    <a class="current" href="#">Home</a><a href="#">Our Team</a><a href="#">Reviews</a><a href="#">Services</a><a href="#">Contact Us</a>
  </nav>
</header>

<section>
  <div class="abs hero" role="img" aria-label="Photo of the dental team standing together in the office"></div>
  <svg class="abs arrow" style="left:76px" width="14" height="26"><path d="M12 2L2 13l10 11" stroke="#fff" stroke-width="1.5" fill="none"/></svg>
  <svg class="abs arrow" style="left:666px" width="14" height="26"><path d="M2 2l10 11L2 24" stroke="#fff" stroke-width="1.5" fill="none"/></svg>
  <p class="abs hero-caption">it's our genuine care and gentle nature that sets us apart!</p>
  <form class="abs booking">
    <h2>SCHEDULE AN APPOINTMENT</h2>
    <div class="field" style="left:102px;width:108px">NAME</div>
    <div class="field" style="left:222px;width:108px">PHONE</div>
    <div class="field" style="left:342px;width:108px">DATE &amp; TIME
      <svg style="position:absolute;right:4px;top:4px" width="10" height="10"><rect x="1" y="2" width="8" height="7" fill="none" stroke="#ec8a2c"/><path d="M1 4h8" stroke="#ec8a2c"/></svg></div>
    <div class="field" style="left:463px;width:108px">MESSAGE</div>
    <div class="submit">SUBMIT</div>
  </form>
</section>

<section>
  <h1 class="abs welcome-title display">Welcome to sunvale dental care</h1>
  <p class="abs welcome-text">Lorem ipsum dolor sit amet, consectetuer adipiscing elit, sed diam nonummy nibh euismod tincidunt ut laoreet dolore magna aliquam erat volutpat. Ut wisi enim ad minim veniam, quis nostrud exerci tation ullamcorper suscipit lobortis nisl ut aliquip ex ea commodo consequat. Duis autem vel eum iriure dolor in hendrerit in vulputate velit esse molestie consequat, vel illum dolore eu feugiat nulla facilisis at vero eros et accumsan et iusto odio dignissim qui blandit praesent luptatum zzril delenit augue duis dolore te feugait nulla facilisi.</p>
  <a class="abs read-more">Read More</a>
  <div class="abs team-photo" role="img" aria-label="Circular photo of the dental team in front of the office logo wall"></div>
</section>

<section>
  <div class="abs band"></div>
  <h2 class="abs section-title" style="left:103px;top:556px">Our <span class="accent">Services</span></h2>
  <div class="abs section-rule" style="left:103px;top:583px;width:328px"></div>

  <div class="abs service active" style="left:105px;top:591px">
    <svg width="36" height="36" viewBox="0 0 36 36"><circle cx="18" cy="18" r="16.5" fill="none" stroke="#ec8a2c" stroke-width="1.5"/><path d="M12 11c2-2 4 0 6 0s4-2 6 0 0 7-1 10-1 6-2 6-1-5-3-5-2 5-3 5-1-3-2-6-3-8-1-10z" fill="none" stroke="#ec8a2c" stroke-width="1.3"/></svg>Exams &amp; Cleaning</div>
  <div class="abs service" style="left:105px;top:634px">
    <svg width="36" height="36" viewBox="0 0 36 36"><circle cx="18" cy="18" r="16.5" fill="none" stroke="#555" stroke-width="1.5"/><path d="M12 14c2-2 4 0 6 0s4-2 6 0 0 6-1 9-1 5-2 5-1-4-3-4-2 4-3 4-1-2-2-5-3-7-1-9z" fill="none" stroke="#555" stroke-width="1.3"/><path d="M18 6v6" stroke="#555" stroke-width="1.3"/></svg>Tooth Colored Fillings</div>
  <div class="abs service" style="left:105px;top:679px">
    <svg width="36" height="36" viewBox="0 0 36 36"><circle cx="18" cy="18" r="16.5" fill="none" stroke="#555" stroke-width="1.5"/><path d="M13 12c2-2 4 0 6 0s4-2 6 0 0 7-1 10-1 6-2 6-1-5-3-5-2 5-3 5-1-3-2-6-3-8-1-10z" fill="#555"/><path d="M7 10h8" stroke="#555" stroke-width="1.5"/></svg>Root Canals</div>
  <div class="abs service" style="left:105px;top:723px">
    <svg width="36" height="36" viewBox="0 0 36 36"><circle cx="18" cy="18" r="16.5" fill="none" stroke="#555" stroke-width="1.5"/><path d="M12 10c2-2 4 0 6 0s4-2 6 0 0 8-1 11-1 6-2 6-1-5-3-5-2 5-3 5-1-3-2-6-3-9-1-11z" fill="#555"/></svg>Crowns</div>

  <div class="abs service" style="left:295px;top:591px">
    <svg width="36" height="36" viewBox="0 0 36 36"><circle cx="18" cy="18" r="16.5" fill="none" stroke="#555" stroke-width="1.5"/><path d="M9 17c0 7 18 7 18 0" fill="none" stroke="#555" stroke-width="2"/><path d="M14 12c1.5-1.5 3 0 4 0s2.5-1.5 4 0 0 5-1 7-1 3-3 3-2-1-3-3-2-5-1-7z" fill="#555"/></svg>Extractions</div>
  <div class="abs service" style="left:295px;top:630px">
    <svg width="36" height="36" viewBox="0 0 36 36"><circle cx="18" cy="18" r="16.5" fill="none" stroke="#555" stroke-width="1.5"/><path d="M6 14h24v5l-2 6h-3l-1-4-2 4h-4l-2-4-2 4H8l-2-6z" fill="#555"/></svg>Bridges</div>
  <div class="abs service" style="left:295px;top:677px">
    <svg width="36" height="36" viewBox="0 0 36 36"><circle cx="18" cy="18" r="16.5" fill="none" stroke="#555" stroke-width="1.5"/><path d="M12 9c2-2 4 0 6 0s4-2 6 0 0 4-2 5H14c-2-1-3-3-2-5z" fill="none" stroke="#555" stroke-width="1.3"/><path d="M15 16h6M15 19h6M16 22h4M17 25h2" stroke="#555" stroke-width="1.5"/></svg>Implants</div>
  <div class="abs service" style="left:295px;top:723px">
    <svg width="36" height="36" viewBox="0 0 36 36"><circle cx="18" cy="18" r="16.5" fill="none" stroke="#555" stroke-width="1.5"/><rect x="8" y="13" width="20" height="10" rx="5" fill="none" stroke="#555" stroke-width="1.5"/><path d="M8 18h20M12 13v10M16 13v10M20 13v10M24 13v10" stroke="#555"/></svg>Dentures</div>

  <h2 class="abs section-title" style="left:480px;top:556px">Office <span class="accent">Hours</span></h2>
  <div class="abs section-rule" style="left:480px;top:583px;width:175px"></div>
  <table class="abs hours">
    <tr><td>Monday</td><td>:</td><td>9am - 6pm</td></tr>
    <tr><td>Tuesday</td><td>:</td><td>9am - 6pm</td></tr>
    <tr><td>Wednesday</td><td>:</td><td>9am - 6pm</td></tr>
    <tr><td>Thursday</td><td>:</td><td>9am - 6pm</td></tr>
    <tr><td>Friday</td><td>:</td><td>Closed</td></tr>
    <tr><td>Saturday</td><td>:</td><td>9am - 6pm</td></tr>
    <tr><td>Sunday</td><td>:</td><td>Closed</td></tr>
  </table>
  <p class="abs emergency">If you have pain or an emergency situation, every attempt will be made to see you the same day.</p>
  <div class="abs hours-phone">
    <svg width="16" height="16" viewBox="0 0 24 24"><circle cx="12" cy="12" r="11" fill="none" stroke="#ec8a2c" stroke-width="1.5"/><path fill="#ec8a2c" d="M9 8l2 2-1 1.5a7 7 0 003 3L14.5 13l2 2-1.5 1.8A9 9 0 017.2 9.5z"/></svg>
    209-555-0148</div>
</section>

<section>
  <h2 class="abs section-title" style="left:0;top:818px;width:758px;text-align:center">Our <span class="accent">Patient Say</span></h2>
  <div class="abs section-rule" style="left:316px;top:844px;width:126px"></div>
  <svg class="abs" style="left:80px;top:895px" width="10" height="14"><path d="M8 1L2 7l6 6" stroke="#999" stroke-width="1.3" fill="none"/></svg>
  <svg class="abs" style="left:668px;top:895px" width="10" height="14"><path d="M2 1l6 6-6 6" stroke="#999" stroke-width="1.3" fill="none"/></svg>
  <blockquote class="abs quote-box"><span class="quote-mark">&ldquo;</span>My experience with Sunvale Dental Care has been awesomw from start to finish. Dr Venn removed several teeth including wisdom teeth with no pain during or after surgery. Excellent work! Thank you, Dr Venn!</blockquote>
  <div class="abs avatar" role="img" aria-label="Portrait photo of the reviewing patient"></div>
  <p class="abs patient">Marcus T Hale</p>
</section>

<section class="abs members">
  <h2 class="section-title" style="position:absolute;left:104px;top:16px">Our <span class="accent">Member of:</span></h2>
  <div class="badge" style="left:311px;width:56px;background:#2e8a3e"></div>
  <div class="badge" style="left:415px;width:52px;background:#9aa0a6"></div>
  <div class="badge" style="left:514px;width:50px;background:#b5bcc4"></div>
</section>

<footer class="abs footer">
  <h3 class="f-head" style="left:103px">Quick Links</h3>
  <div class="f-rule" style="left:103px;width:75px"></div>
  <ul class="f-links"><li>Home</li><li>Our Team</li><li>Reviews</li><li>Services</li><li>Contact Us</li></ul>
  <div class="v-div" style="left:179px"></div>

  <h3 class="f-head" style="left:197px">Contact Details</h3>
  <div class="f-rule" style="left:197px;width:110px"></div>
  <div class="f-contact">
    <div><svg width="8" height="10" viewBox="0 0 8 10"><path d="M4 0a3.5 3.5 0 013.5 3.5C7.5 6 4 10 4 10S.5 6 .5 3.5A3.5 3.5 0 014 0z" fill="#fff"/><circle cx="4" cy="3.5" r="1.3" fill="#ec8a2c"/></svg><span><b>Sunvale Dental Care</b><br>1840 Orchard Way, Linden,<br>CA 95236</span></div>
    <div style="margin-top:2px"><svg width="8" height="9" viewBox="0 0 24 24"><path fill="#fff" d="M6.6 10.8a15 15 0 006.6 6.6l2.2-2.2a1 1 0 011-.25 11.4 11.4 0 003.6.6 1 1 0 011 1V20a1 1 0 01-1 1A17 17 0 013 4a1 1 0 011-1h3.5a1 1 0 011 1c0 1.25.2 2.45.6 3.6a1 1 0 01-.25 1z"/></svg><b style="font-size:8.5px">209-555-0148</b></div>
    <div style="margin-top:4px"><svg width="8" height="8" viewBox="0 0 10 8"><rect width="10" height="8" fill="#fff"/><path d="M0 0l5 4 5-4" stroke="#ec8a2c" fill="none"/></svg>info@sunvaledental.com</div>
  </div>
  <div class="v-div" style="left:327px"></div>

  <h3 class="f-head" style="left:347px">Location Map</h3>
  <div class="map" role="img" aria-label="Street map showing the office location"></div>
  <div class="v-div" style="left:526px"></div>

  <div class="f-brand"><span class="brand-dot"></span><span class="brand-name">sunvale<br>dental care</span></div>
  <span class="social" style="left:585px"></span>
  <span class="social" style="left:602px"></span>
</footer>
<div class="abs copyright">Copyright © Sunvale dental care. All Rights Reserved.</div>

</body>
</html>
```